Plastic Business Card for Bookkeeper

We are looking for a simple professional business card design to use for printing on thin frosted plastic (see-through) card stock. Logo and brand guideline documents are attached as well as a photo of our old business card, and another business card example that we like.

Target Market(s)

Small Business

Industry/Entity Type

Bookkeeper

Contact Information for Business Card

Harriet Valdez CPA
Chief Executive Bookkeeper
T. 03 5926 4187
M. 0432 861 507
E. harriet@quillpathledger.com
W. www.quillpathledger.com

Font styles to use
Sans Serif

Colors
6b449b
00a990

Requirements
Must have
• Stick with logo colors. Writing should be clear and easy to read and not too cramped together.
Nice to have
• Tag line for back of the card - 'Not your ordinary Bookkeeper'

```html
<!DOCTYPE html>
<html lang="en">
<head>
<meta charset="utf-8">
<title>Quillpath Ledger – Business Card</title>
<link rel="stylesheet" href="https://fonts.googleapis.com/css2?family=Roboto:wght@400;500;700&display=swap">
<style>
  :root {
    --stage: #1c1c1c;
    --card: #262626;
    --card-light: #2f2f2f;
    --purple: #6b449b;
    --purple-bright: #7b4fc0;
    --teal: #00a990;
    --ink: #ffffff;
  }
  * { box-sizing: border-box; margin: 0; padding: 0; }
  html, body {
    width: 1200px;
    height: 900px;
    overflow: hidden;
    background: var(--stage);
    font-family: "Roboto", Arial, sans-serif;
  }
  .sheet {
    width: 1200px;
    height: 900px;
    display: flex;
    flex-direction: column;
    align-items: center;
    justify-content: center;
    gap: 40px;
  }
  .card {
    position: relative;
    width: 700px;
    height: 390px;
    background: linear-gradient(135deg, var(--card) 0%, var(--card-light) 100%);
    border-bottom: 5px solid var(--purple-bright);
    box-shadow: 0 12px 30px rgba(0,0,0,.45);
  }
  /* front */
  .card--front {
    display: flex;
    align-items: center;
    justify-content: center;
  }
  .brand {
    display: flex;
    align-items: center;
    gap: 18px;
  }
  .brand__dot {
    width: 26px;
    height: 26px;
    border-radius: 50%;
    background: var(--teal);
    flex-shrink: 0;
  }
  .brand__name {
    font-weight: 700;
    color: var(--purple-bright);
    text-transform: uppercase;
    letter-spacing: 2px;
    font-size: 34px;
    line-height: 1.1;
  }
  /* back */
  .card--back {
    display: flex;
    align-items: center;
    padding: 0 56px;
  }
  .back__brand {
    width: 250px;
    display: flex;
    flex-direction: column;
    align-items: center;
    gap: 16px;
    text-align: center;
  }
  .back__brand .brand__dot { width: 40px; height: 40px; }
  .back__brand .brand__name { font-size: 25px; }
  .divider {
    width: 2px;
    height: 170px;
    background: var(--purple-bright);
    margin: 0 40px 0 20px;
  }
  .contact { color: var(--ink); }
  .contact__name {
    font-size: 31px;
    font-weight: 500;
    color: var(--purple-bright);
  }
  .contact__role {
    font-size: 19px;
    font-weight: 500;
    margin: 2px 0 16px;
  }
  .contact__list { list-style: none; }
  .contact__item {
    display: flex;
    align-items: center;
    gap: 10px;
    font-size: 20px;
    line-height: 1.4;
  }
  .contact__item svg { width: 14px; height: 14px; flex-shrink: 0; }
</style>
</head>
<body>
<main class="sheet">
  <section class="card card--front">
    <div class="brand">
      <span class="brand__dot"></span>
      <span class="brand__name">Quillpath<br>Ledger</span>
    </div>
  </section>

  <section class="card card--back">
    <div class="back__brand">
      <span class="brand__dot"></span>
      <span class="brand__name">Quillpath Ledger</span>
    </div>
    <div class="divider"></div>
    <div class="contact">
      <h1 class="contact__name">Harriet Valdez CPA</h1>
      <p class="contact__role">Chief Executive Bookkeeper</p>
      <ul class="contact__list">
        <li class="contact__item">
          <svg viewBox="0 0 14 14" fill="none" stroke="#7b4fc0" stroke-width="1.5"><path d="M3 1l2 3-1.5 1.5a8 8 0 0 0 5 5L10 9l3 2-1.5 2A11 11 0 0 1 1 2.5z"/></svg>
          03 5926 4187
        </li>
        <li class="contact__item">
          <svg viewBox="0 0 14 14" fill="none" stroke="#7b4fc0" stroke-width="1.5"><rect x="3.5" y="1" width="7" height="12" rx="1"/><line x1="6" y1="11" x2="8" y2="11"/></svg>
          0432 861 507
        </li>
        <li class="contact__item">
          <svg viewBox="0 0 14 14" fill="none" stroke="#7b4fc0" stroke-width="1.5"><rect x="1" y="3" width="12" height="8"/><path d="M1 3l6 5 6-5"/></svg>
          harriet@quillpathledger.com
        </li>
        <li class="contact__item">
          <svg viewBox="0 0 14 14" fill="none" stroke="#7b4fc0" stroke-width="1.3"><circle cx="7" cy="7" r="6"/><ellipse cx="7" cy="7" rx="2.5" ry="6"/><line x1="1" y1="7" x2="13" y2="7"/></svg>
          www.quillpathledger.com
        </li>
      </ul>
    </div>
  </section>
</main>
</body>
</html>
```